Simple Business Card Design for Foodie

Job:

Make a very simple, minimalist business card design with my details including adjusted logo. One side to be white (with logo & text). Other side to be yellow - try plain or with logo (or part of logo eg Z). Need business card to have continuity with website.

Logo:
Our logo is made from a free download font website:
http://www.glyphbarn.net/search.php?q=rubber
but the spacing/kerning needs correcting/adjusting as the font spaces unevenly between letters (see attached files). Need logo to be very crisp/sharp when printed.

Printing:
We will be using Parcly.com so the design needs to conform to their requirements, see here:

http://uk.parcly.com/products/velin/business-cards.html (scroll down for dimensions and guidelines)

Design:

must say "plant-based food consulting" underneath logo or somewhere
no address needed in contact section
sharp corners (not rounded)
one side white, one side yellow

name: Marisol Quenby
1xmobile number: +44 7700 900431
1xtwiiter: @quillcounsel
website address www.greenplatehub.example
email address quill@greenplatehub.example

Should be easy quick job, prompt + detailed feedback given, am online in UK 9am-10pm for next 3 days. Website is www.greenplatehub.example

Must have
• The logo must be corrected. The kerning is not right.

Please use a warm-grey for text

Please submit in matt format, we will be printing matt finish.

Should not have
• Avoid using banners or curvy highlights

Please avoid using black

Please avoid submitting in gloss finish

```html
<!DOCTYPE html>
<html lang="en">
<head>
<meta charset="utf-8">
<title>Quill – Business Card</title>
<link rel="stylesheet" href="https://fonts.googleapis.com/css2?family=Cinzel:wght@400;700&display=swap">
<style>
  :root {
    --backdrop: #6a6a6a;
    --card-white: #ffffff;
    --card-yellow: #f7ef5c;
    --warm-grey: #6b625a;
    --warm-grey-light: #8a8178;
    --accent: #e3d220;
  }
  * { margin: 0; padding: 0; box-sizing: border-box; }
  html, body { width: 1200px; height: 750px; overflow: hidden; }
  body {
    background: var(--backdrop);
    font-family: "Cinzel", serif;
    position: relative;
  }
  .card {
    position: absolute;
    top: 210px;
    width: 525px;
    height: 300px;
  }
  .card--front { left: 68px; background: var(--card-white); }
  .card--back { left: 612px; background: var(--card-yellow); }

  .brand { position: absolute; text-align: center; }
  .card--front .brand { left: 40px; top: 112px; width: 206px; }
  .card--back .brand { left: 0; right: 0; top: 100px; }

  .wordmark {
    font-family: "Cinzel", serif;
    font-weight: 700;
    color: var(--warm-grey);
    line-height: 1;
    letter-spacing: 0.04em;
  }
  .card--front .wordmark { font-size: 50px; }
  .card--back .wordmark { font-size: 76px; }

  .tagline {
    font-family: "Cinzel", serif;
    font-weight: 400;
    color: var(--warm-grey);
    letter-spacing: 0.1em;
    line-height: 1;
  }
  .card--front .tagline { font-size: 9px; margin-top: 14px; }
  .card--back .tagline { font-size: 13px; margin-top: 20px; }

  .divider {
    position: absolute;
    left: 261px;
    top: 98px;
    width: 2px;
    height: 98px;
    background: linear-gradient(to bottom, rgba(227,210,32,0), var(--accent) 50%, rgba(227,210,32,0));
  }

  .details { position: absolute; left: 289px; top: 108px; }
  .details__name {
    color: var(--warm-grey);
    font-weight: 700;
    font-size: 15px;
    line-height: 1;
  }
  .details__role {
    color: var(--warm-grey-light);
    font-size: 12px;
    margin-top: 4px;
    line-height: 1;
  }
  .contact { list-style: none; margin-top: 12px; }
  .contact__item {
    display: flex;
    align-items: center;
    gap: 9px;
    color: var(--warm-grey);
    font-size: 11.5px;
    height: 15px;
    letter-spacing: 0.01em;
  }
  .contact__icon { width: 13px; height: 11px; flex: none; fill: var(--accent); }
</style>
</head>
<body>
  <section class="card card--front">
    <div class="brand">
      <div class="wordmark">QUILL</div>
      <div class="tagline">Plant-based food consulting</div>
    </div>
    <div class="divider"></div>
    <div class="details">
      <div class="details__name">Marisol Quenby</div>
      <div class="details__role">Manager</div>
      <ul class="contact">
        <li class="contact__item">
          <svg class="contact__icon" viewBox="0 0 13 11" aria-hidden="true"><path d="M1 3.5C1 2 3 1 6.5 1S12 2 12 3.5L10 4.5 9 3H4L3 4.5ZM3.5 5h6L11 10H2Z"/></svg>
          <span>+44 7700 900431</span>
        </li>
        <li class="contact__item">
          <svg class="contact__icon" viewBox="0 0 13 11" aria-hidden="true"><path d="M1 1h11v9H1Zm1.2 1.2L6.5 6l4.3-3.8v-.2H2.2ZM2 9h9V3.6L6.5 7.5 2 3.6Z"/></svg>
          <span>quill@greenplatehub.example</span>
        </li>
        <li class="contact__item">
          <svg class="contact__icon" viewBox="0 0 13 11" aria-hidden="true"><path d="M1 1h11v7H1Zm1 1v5h9V2ZM4 9h5v1H4Z"/></svg>
          <span>www.greenplatehub.example</span>
        </li>
      </ul>
    </div>
  </section>

  <section class="card card--back">
    <div class="brand">
      <div class="wordmark">QUILL</div>
      <div class="tagline">Plant-based food consulting</div>
    </div>
  </section>
</body>
</html>
```